Banner Ad Design Project for responsive website

Looking to update the main banner on my website www.bridalpathly.com but it will be for our new responsive website, you can see here http://www.bridalpathly.com/dev/
Banner should be 300 px high by1920 pix wide
Please contact me with any questions
Should include:
All the text from the existing banner ie
Bridal Show
THE FIRST 50 BRIDES WILL GET A CHANCE TO WIN $25000
Honeymoon Cruise Giveaway
"Pick the Perfect Gown" casting call
Banner should be 1920 pix wide
Final delivery will require layered psd file and all fonts

Target Market(s)

Brides

Industry/Entity Type

Call

Requirements
Must have
• All the text from the existing banner ie
• Bridal Show
• THE FIRST 50 BRIDES WILL GET A CHANCE TO WIN $25000
• Honeymoon Cruise Giveaway
• "Pick the Perfect Gown" casting call
• Banner should be 1920 pix wide
Nice to have
• The look and feel of our postcard, see attached
Should not have
• Any specifics to any date/time/location as the banner will be online all the time and the specifics for each show will be different

```html
<!DOCTYPE html>
<html lang="en">
<head>
<meta charset="utf-8">
<title>Bridal Show Banner</title>
<link rel="stylesheet" href="https://fonts.googleapis.com/css2?family=Great+Vibes&family=Arimo:ital,wght@0,400;0,700;1,400&display=swap">
<style>
  :root{
    --stage:#1c1c1c;
    --paper:#f7f7f7;
    --paper-shade:#e4e4e4;
    --green:#0f6a12;
    --green-dark:#0b4d0d;
    --green-photo:#2f7a2a;
    --blue:#4aa8ef;
    --blue-light:#86c6f6;
    --blue-script:#2a6fb8;
    --grey-text:#3c3c3c;
    --white:#ffffff;
  }
  html,body{margin:0;padding:0;width:1200px;height:1000px;overflow:hidden;background:var(--stage);}
  .banner{position:absolute;left:74px;top:418px;width:1053px;height:163px;overflow:hidden;
    background:linear-gradient(180deg,var(--white),var(--paper) 60%,var(--paper-shade));
    box-shadow:0 6px 14px rgba(0,0,0,.6);font-family:"Arimo",Arial,sans-serif;}
  .bride-photo{position:absolute;left:0;top:0;width:135px;height:163px;
    background:linear-gradient(160deg,#3d8d34,var(--green-photo) 55%,#1f5a1c);}
  .photo-edge{position:absolute;left:90px;top:0;width:46px;height:163px;}
  .bells{position:absolute;top:12px;width:72px;height:50px;border-radius:20px;
    background:radial-gradient(ellipse at center,rgba(15,106,18,.18),rgba(15,106,18,0) 70%);}
  .bells.left{left:118px}
  .bells.right{left:505px}
  .show-title{position:absolute;left:196px;top:6px;margin:0;font-family:"Great Vibes",cursive;
    font-weight:400;font-size:60px;color:var(--green);line-height:64px;white-space:nowrap;}
  .details-button{position:absolute;left:159px;top:77px;width:109px;height:21px;
    background:linear-gradient(180deg,#2f8f2f,var(--green-dark));color:var(--white);
    font-size:13px;line-height:21px;text-align:center;border-radius:2px;}
  .cruise-photo{position:absolute;left:159px;top:104px;width:109px;height:55px;border-radius:2px;
    background:linear-gradient(180deg,#8fd0f3 0%,#cfeefc 45%,#3b9ad8 70%,#1f6fb0 100%);}
  .admission{position:absolute;left:289px;top:76px;margin:0;font-size:22.5px;font-weight:700;color:var(--green);}
  .admission sup{font-size:12px;vertical-align:8px}
  .cruise-line{position:absolute;left:290px;top:103px;margin:0;font-family:"Great Vibes",cursive;
    font-size:25px;line-height:28px;color:var(--blue-script);white-space:nowrap;}
  .meet-line{position:absolute;left:289px;top:135px;margin:0;font-size:14.2px;font-style:italic;color:var(--grey-text);white-space:nowrap;}
  .prize-panel{position:absolute;left:585px;top:0;width:468px;height:163px;}
  .dice{position:absolute;left:634px;top:46px;width:118px;height:62px;border-radius:8px;
    background:linear-gradient(135deg,#7cc4f7,#1f7fd0);}
  .prize-lead{position:absolute;left:770px;top:24px;margin:0;font-size:19px;line-height:19px;color:var(--white);white-space:nowrap;}
  .prize-amount{position:absolute;left:769px;top:63px;margin:0;font-size:33.5px;line-height:33px;color:var(--white);white-space:nowrap;}
  .casting-call{position:absolute;left:770px;top:136px;margin:0;font-size:12px;line-height:14px;font-style:italic;color:var(--white);white-space:nowrap;}
</style>
</head>
<body>
<div class="banner">
  <div class="bride-photo" role="img" aria-label="Photo of a bride in a strapless gown against green foliage"></div>
  <svg class="photo-edge" viewBox="0 0 46 163" aria-hidden="true">
    <path d="M46 0 H10 C-4 40 34 70 24 110 C18 135 8 150 10 163 H46 Z" fill="#f7f7f7"/>
  </svg>

  <div class="bells left" role="img" aria-label="Wedding bells ornament"></div>
  <h1 class="show-title">Bridal Show</h1>
  <div class="bells right" role="img" aria-label="Wedding bells ornament"></div>

  <div class="details-button">Click for Details</div>
  <div class="cruise-photo" role="img" aria-label="Photo of a cruise ship on blue sea"></div>

  <p class="admission"><sup>$</sup>8 Admission</p>
  <p class="cruise-line">Plus a Caribbean Cruise Giveaway</p>
  <p class="meet-line">Come and meet the area's best professionals</p>

  <svg class="prize-panel" viewBox="0 0 468 163" preserveAspectRatio="none" aria-hidden="true">
    <path d="M32 0 C0 40 -4 120 32 163 H468 V0 Z" fill="#86c6f6"/>
    <path d="M42 0 C12 40 8 120 42 163 H468 V0 Z" fill="#4aa8ef"/>
  </svg>
  <div class="dice" role="img" aria-label="Two blue dice"></div>
  <p class="prize-lead">The First 50 Brides will roll<br>the dice for a chance to win</p>
  <p class="prize-amount">$25,000 for your<br>Dream Wedding</p>
  <p class="casting-call">"Pick the Perfect Gown" casting call</p>
</div>
</body>
</html>
```